Make a creative business cards for our agency

We are a creative, digital marketing and IT development agency. We need a new: flat design, modern-corporate, not much elements, two sided business cards based in our logo (which I provide here in jpg and psd).

We prefer a vertical design, please no, qr codes no complex backgrounds, NO TEMPLATES.

We want to include:

Logo/Name of the agency
Slogan
Name
Title
Email
Phone
Web url
Social Media (Facebook, Twitter and Youtube)
You can simulate all this info and just place invented info.

Feel free to propose. Very important is to keep the same dark red color of the logo for a big area in the background of your design, keep the same font type preferably, you can get off of the box I you consider your idea is great.

In the case you need extra material or more brief info, just let me know please.

```html
<!DOCTYPE html>
<html lang="en">
<head>
<meta charset="UTF-8">
<title>Norvale Studio – Business Cards</title>
<link href="https://fonts.googleapis.com/css2?family=Lato:wght@300;400;700&display=swap" rel="stylesheet">
<style>
  :root {
    --stage: #46484b;
    --card-red: #6a0b12;
    --card-red-deep: #560910;
    --ink: #ffffff;
    --ink-soft: rgba(255,255,255,0.85);
  }
  * { margin: 0; padding: 0; box-sizing: border-box; }
  html, body { width: 1200px; height: 900px; overflow: hidden; }
  body {
    background: var(--stage);
    font-family: "Lato", sans-serif;
    color: var(--ink);
    position: relative;
  }
  .card {
    position: absolute;
    left: 280px;
    width: 640px;
    height: 366px;
    border-radius: 16px;
    background: linear-gradient(160deg, var(--card-red) 0%, var(--card-red-deep) 100%);
    overflow: hidden;
  }
  .card--front { top: 62px; }
  .card--back { top: 472px; }

  .rule {
    position: absolute;
    height: 2px;
    background: var(--ink-soft);
  }

  /* brand lockup */
  .brand {
    position: absolute;
    display: flex;
    flex-direction: column;
    align-items: center;
  }
  .brand__dot {
    width: 64px; height: 64px;
    border-radius: 50%;
    background: var(--ink);
    margin-bottom: 12px;
  }
  .brand__name {
    font-weight: 300;
    font-size: 40px;
    letter-spacing: 0.5px;
    white-space: nowrap;
  }

  /* front side */
  .card--front .brand { left: 0; right: 0; top: 46px; }
  .card--front .rule--left { left: 0; width: 150px; top: 160px; }
  .card--front .rule--right { right: 0; width: 150px; top: 160px; }

  .contact {
    position: absolute;
    right: 34px;
    top: 212px;
    text-align: right;
  }
  .contact__name { font-weight: 700; font-size: 24px; }
  .contact__title { font-weight: 300; font-size: 14px; margin-top: 3px; margin-bottom: 14px; }
  .contact__row {
    display: flex;
    justify-content: flex-end;
    align-items: center;
    gap: 12px;
    font-weight: 300;
    font-size: 14px;
    line-height: 1.25;
    margin-top: 6px;
  }
  .contact__row svg { width: 16px; height: 16px; flex: none; fill: var(--ink); }

  /* back side */
  .card--back .brand { left: 0; right: 0; top: 34px; }
  .card--back .brand__dot { width: 56px; height: 56px; margin-bottom: 10px; }
  .slogan { font-weight: 300; font-size: 16px; margin-top: 4px; }
  .url { font-weight: 700; font-size: 15px; margin-top: 8px; }
  .card--back .rule--left { left: 0; width: 140px; top: 210px; }
  .card--back .rule--right { right: 0; width: 140px; top: 210px; }

  .socials {
    position: absolute;
    left: 0; right: 0;
    bottom: 40px;
    display: flex;
    justify-content: space-around;
    padding: 0 30px;
  }
  .social {
    display: flex;
    flex-direction: column;
    align-items: center;
    gap: 10px;
    font-weight: 300;
    font-size: 15px;
  }
  .social__dot {
    width: 24px; height: 24px;
    border-radius: 50%;
    background: var(--ink);
  }
</style>
</head>
<body>

  <section class="card card--front" aria-label="Business card front">
    <div class="rule rule--left"></div>
    <div class="rule rule--right"></div>
    <div class="brand">
      <span class="brand__dot"></span>
      <span class="brand__name">Norvale Studio</span>
    </div>
    <div class="contact">
      <div class="contact__name">Marcus Keller</div>
      <div class="contact__title">CEO, Norvale Studio</div>
      <div class="contact__row">
        <span>+41 76 555 01 23</span>
        <svg viewBox="0 0 24 24" aria-hidden="true"><path d="M6.6 10.8a15.1 15.1 0 0 0 6.6 6.6l2.2-2.2a1 1 0 0 1 1-.25 11.4 11.4 0 0 0 3.6.57 1 1 0 0 1 1 1V20a1 1 0 0 1-1 1A17 17 0 0 1 3 4a1 1 0 0 1 1-1h3.5a1 1 0 0 1 1 1c0 1.25.2 2.45.57 3.57a1 1 0 0 1-.25 1z"/></svg>
      </div>
      <div class="contact__row">
        <span>marcus@norvalestudio.ch</span>
        <svg viewBox="0 0 24 24" aria-hidden="true"><path d="M2 21 23 12 2 3v7l15 2-15 2z"/></svg>
      </div>
      <div class="contact__row">
        <span>8050 Talacker Zürich<br>Switzerland</span>
        <svg viewBox="0 0 24 24" aria-hidden="true"><path d="M12 2a7 7 0 0 0-7 7c0 5.25 7 13 7 13s7-7.75 7-13a7 7 0 0 0-7-7zm0 9.5A2.5 2.5 0 1 1 12 6.5a2.5 2.5 0 0 1 0 5z"/></svg>
      </div>
    </div>
  </section>

  <section class="card card--back" aria-label="Business card back">
    <div class="rule rule--left"></div>
    <div class="rule rule--right"></div>
    <div class="brand">
      <span class="brand__dot"></span>
      <span class="brand__name">Norvale Studio</span>
      <span class="slogan">Web, Visual, IT &amp; Mkt Solutions</span>
      <span class="url">www.norvalestudio.ch</span>
    </div>
    <div class="socials">
      <div class="social"><span class="social__dot"></span><span>vidhub.net/norvale</span></div>
      <div class="social"><span class="social__dot"></span><span>chirp.net/norvale</span></div>
      <div class="social"><span class="social__dot"></span><span>friendsbook.net/norvale</span></div>
    </div>
  </section>

</body>
</html>
```